Word template Letterhead for Australian Law Firm

We are a small law firm based in Manly, NSW, Australia. We have had a new logo designed for us and wish to freshen up the appearance of our letterhead. We require the letterhead to be in a word document that we can type over. This will not be a ‘printed’ letterhead because we send the majority of our correspondence via email. We would like to see a few options. We have attached our previous letterhead as well as the artwork for our new logo. We like the idea of a watermark across the bottom of the letter but the watermark must stay in place and we must be able to type over it. We are open to some colour throughout the letterhead because the majority of our correspondence is sent electronically. We also use electronic signatures. I have uploaded an example of this.The letterhead must include:-1. Our address details – including our phone number, physical address, website address etc. These details can be found on the copy of our previous letterhead;2. ABN Number;3. The words ‘Brevicor (NSW) Pty Ltd ACN 482 731 058 trading as Shipton & AssociatesLiability limited by a scheme approved under Professional Standards Legislation. The letterhead does not need to include the names and qualifications of the people working at the firm. Thank you.

Target Market(s)

Clients and other parties

Industry/Entity Type

Law Firm

Font styles to use
Other font styles liked:
• raleway, montserrat

Colors

Designer to choose colors to be used in the design.

Requirements
Must have
• Certain wording - please see project description.
• Must be a word document and must be able to type over the watermark etc.
Nice to have
• Watermark at the bottom of the letter.

```html
<!DOCTYPE html>
<html lang="en">
<head>
<meta charset="utf-8">
<title>Kervell &amp; Associates – Letterhead</title>
<link href="https://fonts.googleapis.com/css2?family=Abel&family=Carlito:ital,wght@0,400;0,700;1,400&family=Raleway:wght@600&display=swap" rel="stylesheet">
<style>
  :root {
    --navy: #142a5c;
    --brand-blue: #3d4a9a;
    --gold: #f0c02a;
    --text-grey: #6b6b6b;
    --soft-grey: #707070;
    --watermark-a: rgba(120, 135, 200, 0.10);
    --watermark-b: rgba(200, 180, 120, 0.08);
    --paper: #ffffff;
  }
  * { margin: 0; padding: 0; box-sizing: border-box; }
  html, body { width: 848px; height: 1200px; overflow: hidden; background: var(--paper); }
  .letterhead {
    position: relative; width: 848px; height: 1200px;
    font-family: "Carlito", "Calibri", sans-serif; color: var(--text-grey);
  }
  .abs { position: absolute; }

  .brand { left: 68px; top: 190px; display: flex; align-items: center; gap: 10px; }
  .brand-dot { width: 14px; height: 14px; border-radius: 50%; background: var(--brand-blue); }
  .brand-name {
    font-family: "Raleway", sans-serif; font-weight: 600; font-size: 17px;
    letter-spacing: 1.4px; color: var(--brand-blue);
  }

  .contact {
    right: 66px; top: 124px; text-align: right;
    font-family: "Abel", sans-serif; font-size: 11.4px; color: var(--text-grey); letter-spacing: 0.3px;
  }
  .contact p { position: absolute; right: 0; white-space: nowrap; }
  .contact .web { font-weight: 700; font-family: "Carlito", sans-serif; font-size: 11.6px; }

  .rule-gold { left: 138px; top: 273px; width: 584px; height: 1.5px; background: var(--gold); }
  .rule-navy { left: 138px; top: 1107px; width: 584px; height: 1.5px; background: var(--navy); }

  .refs { left: 86px; top: 310px; font-family: "Abel", sans-serif; font-size: 10px; }
  .refs p { height: 24px; }
  .date { right: 66px; top: 359px; font-family: "Abel", sans-serif; font-size: 13px; }
  .date sup { font-size: 7px; }
  .salutation { left: 71px; top: 395px; font-family: "Abel", sans-serif; font-size: 13px; }
  .subject { left: 71px; top: 437px; font-family: "Carlito", sans-serif; font-weight: 700; font-size: 16px; color: var(--navy); }

  .watermark {
    left: 70px; top: 580px; width: 740px; height: 300px; border-radius: 150px 150px 200px 60px;
    background: radial-gradient(ellipse at 30% 40%, var(--watermark-a), transparent 70%),
                radial-gradient(ellipse at 75% 70%, var(--watermark-b), transparent 65%);
  }

  .body-copy { left: 71px; top: 478px; width: 720px; font-size: 13px; line-height: 34.7px; }
  .body-copy p { margin-bottom: 34.7px; }

  .closing { left: 71px; top: 920px; font-family: "Abel", sans-serif; font-size: 11.5px; line-height: 21px; }
  .signature { left: 74px; top: 970px; width: 93px; height: 34px; background: linear-gradient(90deg, #f2f2f2, #e6e6e6); border-right: 1px solid #ddd; }
  .signatory { left: 71px; top: 1022px; font-family: "Abel", sans-serif; font-weight: 400; font-size: 13px; letter-spacing: 0.3px; }
  .signatory-email { left: 71px; top: 1047px; font-family: "Abel", sans-serif; font-size: 11.5px; }

  .accreditation { left: 580px; top: 966px; display: flex; align-items: center; gap: 12px; }
  .badge { width: 50px; height: 50px; border-radius: 50%; background: #2e8fc9; }
  .accreditation-text { font-weight: 700; font-size: 9.5px; line-height: 12px; color: var(--soft-grey); letter-spacing: 0.2px; }

  .footer { left: 0; width: 848px; top: 1138px; text-align: center; font-size: 8.6px; color: var(--soft-grey); line-height: 18px; }
  .footer .legal { font-style: italic; }
</style>
</head>
<body>
<main class="letterhead">
  <div class="abs brand">
    <span class="brand-dot"></span>
    <span class="brand-name">Kervell &amp; Associates</span>
  </div>

  <address class="abs contact">
    <p style="top:0">SUITE 4, 18 CORELLA STREET MANLY&nbsp; NSW&nbsp; 2095</p>
    <p style="top:34px">Tel: (02) 9000 4812 / Fax: (02) 9000 4813</p>
    <p style="top:55px">E-mail: reception@brevicorlaw.com.au&nbsp;&nbsp; ABN: 64 482 731 058</p>
    <p class="web" style="top:76px">www.kervellassociates.com.au</p>
  </address>

  <div class="abs rule-gold"></div>

  <div class="abs watermark" role="img" aria-label="Faint brand watermark across the lower letter"></div>

  <div class="abs refs">
    <p>OUR REF: HM:DHR:4182</p>
    <p>YOUR REF: Daniel Harrow</p>
  </div>
  <p class="abs date">15<sup>TH</sup> September 2019</p>
  <p class="abs salutation">Dear Sir/ Madam,</p>
  <h1 class="abs subject">RE: LETTERHEAD</h1>

  <div class="abs body-copy">
    <p style="margin-bottom:0">A letterhead is the heading at the top of a sheet of letter paper (stationery).<br>That heading usually consists of a name and an address, and a logo or corporate design, and sometimes a background pattern. The term "letterhead" is often used to refer to the whole sheet imprinted with such a heading. Many companies and individuals prefer to create a letterhead template in a word processor or other software application.</p>
    <p style="margin-top:34.7px">This generally includes the same information as pre-printed stationery but without the additional costs involved. Letterhead can then be printed on stationery (or plain paper) as needed on a local output device or sent electronically. That heading usually consists of a name and an address, and a logo or corporate design, and sometimes a background pattern. The term "letterhead" is often used to refer to the whole sheet imprinted with such a heading.</p>
    <p>The term "letterhead" is often used to refer to the whole sheet imprinted with such a heading. Many companies and individuals prefer to create a letterhead template in a word processor or other software application.</p>
  </div>

  <div class="abs closing">
    <p>Yours faithfully</p>
    <p>KERVELL &amp; ASSOCIATES</p>
  </div>
  <div class="abs signature" role="img" aria-label="Electronic signature"></div>
  <p class="abs signatory">HELEN MARSH</p>
  <p class="abs signatory-email">Direct Email: helen@brevicorlaw.com.au</p>

  <div class="abs accreditation">
    <span class="badge" aria-hidden="true"></span>
    <p class="accreditation-text">ACCREDITED SPECIALIST<br>FAMILY LAW</p>
  </div>

  <div class="abs rule-navy"></div>

  <footer class="abs footer">
    <p>Brevicor (NSW) Pty Ltd ACN 482 731 058 trading as Kervell &amp; Associates</p>
    <p class="legal">Liability limited by a scheme approved under Professional Standards Legislation. Legal practitioners at</p>
    <p class="legal">Brevicor (NSW) Pty Ltd are members of the scheme.</p>
  </footer>
</main>
</body>
</html>
```